Young and modern Electrical company working in the commercial arena.

Wanting a business card design thats modern and will last. Maybe Minimalist? Happy to look at changing my logo

Target Market(s)

Builders, Project Managers

Industry/Entity Type

Electrical

Contact Information for Business Card

Name
Address
Phone number
Job title

Logo Text

our name or just the logo i'm open to ideas

Font styles to use
Sans Serif

Requirements
Nice to have
• would like to keep the purple in our current logo. it's kinda unique to our market
Should not have
• Don't want it to be to busy. simple is best i think

```html
<!DOCTYPE html>
<html lang="en">
<head>
<meta charset="utf-8">
<title>Halvorsen Electrical – Business Cards</title>
<link rel="stylesheet" href="https://fonts.googleapis.com/css2?family=Open+Sans:wght@400;600&display=swap">
<style>
  :root {
    --bg: #e9e7e3;
    --card-white: #fdfdfd;
    --card-dark: #1d211f;
    --ink: #2a2a2a;
    --ink-soft: #3b3b3b;
    --purple: #7b4fc4;
    --white: #ffffff;
  }
  * { box-sizing: border-box; margin: 0; padding: 0; }
  html, body {
    width: 1200px; height: 1000px; overflow: hidden;
    background: var(--bg);
    font-family: "Open Sans", Arial, sans-serif;
  }
  .canvas {
    position: relative; width: 1200px; height: 1000px;
  }
  .card {
    position: absolute;
    width: 560px; height: 320px;
    left: 320px;
    background: var(--card-white);
    box-shadow: 0 6px 18px rgba(0,0,0,0.15);
    overflow: hidden;
  }
  .card--front { top: 130px; }
  .card--back { top: 540px; }

  .wordmark {
    color: var(--purple);
    font-weight: 600;
    letter-spacing: 0.5px;
    text-transform: lowercase;
    display: flex; align-items: center; gap: 10px;
  }
  .wordmark__dot {
    width: 14px; height: 14px; border-radius: 50%;
    background: var(--purple);
  }
  .card--front .wordmark {
    position: absolute; left: 0; right: 0; top: 0; bottom: 0;
    justify-content: center;
    font-size: 40px;
  }

  .back__split {
    position: absolute; inset: 0; width: 100%; height: 100%;
  }
  .back__brand {
    position: absolute; top: 34px; right: 34px;
    text-align: right;
  }
  .back__brand .wordmark { font-size: 24px; justify-content: flex-end; }
  .back__tagline {
    color: var(--purple); font-size: 13px; margin-top: 4px;
  }
  .contact {
    position: absolute; left: 30px; top: 40px;
    list-style: none;
    font-size: 13px; color: var(--ink-soft);
    line-height: 1.45;
  }
  .contact li { display: flex; align-items: flex-start; gap: 9px; margin-bottom: 4px; }
  .contact svg { flex: none; margin-top: 3px; }
  .person {
    position: absolute; right: 40px; bottom: 40px; text-align: right;
  }
  .person__name { color: var(--white); font-size: 28px; font-weight: 400; }
  .person__role { color: var(--purple); font-size: 17px; letter-spacing: 1px; }
</style>
</head>
<body>
<main class="canvas">

  <section class="card card--front" aria-label="Business card front">
    <div class="wordmark"><span class="wordmark__dot"></span>halvorsen electrical</div>
  </section>

  <section class="card card--back" aria-label="Business card back">
    <svg class="back__split" viewBox="0 0 560 320" preserveAspectRatio="none" aria-hidden="true">
      <polygon points="150,320 560,120 560,320" fill="var(--card-dark)"/>
    </svg>

    <div class="back__brand">
      <div class="wordmark">halvorsen electrical</div>
      <div class="back__tagline">Electrical Services</div>
    </div>

    <ul class="contact">
      <li>
        <svg width="10" height="12" viewBox="0 0 10 12" aria-hidden="true"><rect x="1" y="0.5" width="8" height="11" rx="1.5" fill="none" stroke="var(--purple)" stroke-width="1.2"/></svg>
        0400 123 987
      </li>
      <li>
        <svg width="12" height="10" viewBox="0 0 12 10" aria-hidden="true"><rect x="0.5" y="0.5" width="11" height="9" fill="var(--purple)"/><path d="M0.5 0.5 L6 5.5 L11.5 0.5" fill="none" stroke="#fff" stroke-width="1"/></svg>
        dane@halvorsenelectrical.com.au
      </li>
      <li>
        <svg width="12" height="12" viewBox="0 0 12 12" aria-hidden="true"><circle cx="6" cy="6" r="5.5" fill="var(--purple)"/><path d="M0.5 6 H11.5 M6 0.5 V11.5" stroke="#fff" stroke-width="0.9"/></svg>
        www.halvorsenelectrical.com.au
      </li>
      <li>
        <svg width="12" height="12" viewBox="0 0 12 12" aria-hidden="true"><circle cx="6" cy="6" r="5" fill="none" stroke="var(--purple)" stroke-width="1.5"/><circle cx="6" cy="6" r="2" fill="var(--purple)"/></svg>
        <span>your address your address,<br>your address</span>
      </li>
    </ul>

    <div class="person">
      <div class="person__name">Dane Whitby</div>
      <div class="person__role">owner</div>
    </div>
  </section>

</main>
</body>
</html>
```